Long Established Local Fencing (not swords) Business needs fresh Business Cards

We need fresh double sided business cards for our Fencing Construction business, we are looking for something with our new logo design added, and maybe a photo background ?
We recently had cards made from Cardlyne and we were horrified with what we got back, the quality was terrible, so am looking for high quality format for good printing company to make.
We install Steelmora, Timber paling, Aluminium Slat Screening, Picket (timber and aluminium) and most other fencing installations.
Our website is brankelrails.com.au should you like to learn a bit more.
We do have logo in other formats if required.
We have been in business for over 35 years and we have used this as a "motto" it is on our signage

Industry/Entity Type

Construction

Contact Information for Business Card

Open to ideas, we need 3 x different cards, one generic with no name and 2 x others each with 1 of our bosses name on each, I will put into upload files.

Colors
ec1f27
000000
606060
f5f5f5

Requirements
Must have
• Company Name and Logo
• Address
• Contact details, phone, website, email etc
• Small space to write notes when leaving card at residence
Nice to have
• Our motto "Servicing the Peninsula for over 35 years"

```html
<!DOCTYPE html>
<html lang="en">
<head>
<meta charset="utf-8">
<title>Brankel Rails – Business Cards</title>
<link rel="stylesheet" href="https://fonts.googleapis.com/css2?family=Roboto:ital,wght@0,400;0,700;0,900;1,400&family=Roboto+Condensed:wght@500&display=swap">
<style>
  :root {
    --brand-red: #ec1f27;
    --brand-black: #000000;
    --brand-grey: #606060;
    --card-white: #f5f5f5;
    --text-grey: #555555;
    --backdrop: #2b2b2b;
    --rule: #cfcfcf;
  }
  * { margin: 0; padding: 0; box-sizing: border-box; }
  html, body {
    width: 1200px; height: 960px; overflow: hidden;
    background: var(--backdrop);
    font-family: "Roboto", Arial, sans-serif;
  }
  .canvas { position: relative; width: 1200px; height: 960px; }
  .card {
    position: absolute; left: 320px; width: 600px; height: 344px;
    background: var(--card-white);
  }
  .card--front { top: 104px; }
  .card--back { top: 492px; }

  /* front */
  .brand-block {
    position: absolute; left: 40px; top: 150px; width: 238px;
    display: flex; align-items: center; justify-content: center; gap: 10px;
  }
  .brand-square { width: 16px; height: 16px; background: var(--brand-red); flex: none; }
  .brand-name {
    font-weight: 900; font-size: 27px; letter-spacing: 0.5px;
    color: var(--brand-black); text-transform: uppercase; white-space: nowrap;
  }
  .divider {
    position: absolute; left: 288px; top: 90px; width: 1px; height: 180px;
    background: var(--rule);
  }
  .contact { position: absolute; left: 317px; top: 88px; color: var(--text-grey); }
  .contact__name {
    font-family: "Roboto Condensed", "Arial Narrow", sans-serif;
    font-weight: 500; font-size: 21px; color: var(--brand-red);
    text-transform: uppercase; line-height: 1; margin-bottom: 10px;
  }
  .contact__details { font-size: 14px; line-height: 18px; margin-bottom: 11px; }
  .contact__list { list-style: none; font-size: 14px; line-height: 19px; }
  .contact__list li { display: flex; align-items: center; gap: 9px; }
  .contact__list svg { width: 12px; height: 12px; fill: var(--brand-red); flex: none; }

  /* back */
  .brand-block--back { left: 0; top: 52px; width: 600px; }
  .brand-block--back .brand-name { font-size: 25px; }
  .notes { position: absolute; left: 48px; top: 131px; width: 500px; }
  .notes__line { height: 35px; border-top: 1px dotted #444; }
  .motto {
    position: absolute; left: 0; top: 302px; width: 600px; text-align: center;
    font-style: italic; font-size: 14px; color: var(--text-grey);
  }
</style>
</head>
<body>
<main class="canvas">
  <section class="card card--front" aria-label="Business card front">
    <div class="brand-block">
      <span class="brand-square"></span>
      <span class="brand-name">Brankel Rails</span>
    </div>
    <div class="divider"></div>
    <div class="contact">
      <h1 class="contact__name">Darren Kettle</h1>
      <p class="contact__details">42 Reddan Ave Pellin<br>License No: 51274k<br>ABN 63 218 90 547</p>
      <ul class="contact__list">
        <li><svg viewBox="0 0 12 12"><path d="M2.4 0.6l2 2.2-1 1.4c.7 1.6 1.9 2.8 3.4 3.4l1.4-1 2.2 2-1.2 2.2C5 10.6 1.4 7 0.4 1.8z"/></svg>(02)40918826</li>
        <li><svg viewBox="0 0 12 12"><path d="M3 0h6a1 1 0 0 1 1 1v10a1 1 0 0 1-1 1H3a1 1 0 0 1-1-1V1a1 1 0 0 1 1-1zm.6 1.4v8h4.8v-8z"/></svg>0428 506 731</li>
        <li><svg viewBox="0 0 12 12"><path d="M0 2.5h12v7H0zM0.8 3.1L6 6.8l5.2-3.7z" fill-rule="evenodd"/></svg>brankelrails@netlane.com</li>
        <li><svg viewBox="0 0 12 12"><circle cx="6" cy="6" r="5.6"/><path d="M3 3.5c1 .2 1.6 1 1.4 2-.3 1 1 1.4 1 2.6M8.5 2.5c-.6 1-.2 2 .8 2.3M7.5 10c.2-1 1-1.6 1.8-1.6" stroke="#f5f5f5" stroke-width=".9" fill="none"/></svg>www.brankelrails.com.au</li>
      </ul>
    </div>
  </section>

  <section class="card card--back" aria-label="Business card back">
    <div class="brand-block brand-block--back">
      <span class="brand-square"></span>
      <span class="brand-name">Brankel Rails</span>
    </div>
    <div class="notes" aria-label="Space for notes">
      <div class="notes__line"></div>
      <div class="notes__line"></div>
      <div class="notes__line"></div>
      <div class="notes__line"></div>
      <div class="notes__line"></div>
    </div>
    <p class="motto">Servicing the Peninsula for over 35 years</p>
  </section>
</main>
</body>
</html>
```